Advertising flyer for proofreading business.

Hello everyone,

I need an advertising flyer for a new proofreading company in Australia.

I would like your design in be in two sizes:
- A4 (to be posted on noticeboards),
- A6 (to be printed in larger quantity to give away)
(please see the size specification file attached).

The text file is attached (Ad Text) and it contains lots of information. Please feel free to include your choice of text from the text file, but please include Poster title, and highlight 'ESL' and students discounts.

I understand that it is impossible to include the same amount of information on A6 and A4, so please feel free to chose what fits on each of them, but please keep the design similar.

I have attached our company logo, but feel free to adjust it to the poster design (feel free to change the color as well). The original logo file contains circle around it, please feel free to remove it and include only the typeset as it can be seen here: http://www.vellumcheck.com.au/.

Flyers will be printed, so please see the specification file for details.

I will do my best to respond to feedback as soon as possible.

I appreciate your participation, time and help,
Best wishes,
Radoslaw

Target Market(s)

Students, authors

Industry/Entity Type

Business

Colors

Designer to choose colors to be used in the design.

Requirements
Must have
• It would be good if poster is easy to spot on busy noticeboards and attract attention.
• Please keep the poster in the positive/optimistic mood, and so that it focuses on students, maybe photos of graduates(?).
• Poster title,
• Please include the list of proof-read documents as they are described in the attached text file (Ad Text).
• Please highlight students discounts and ESL.
Nice to have
• I would like to leave the creative freedom to all designers so at this point I have not adjusted the Look and Feel sliders. Please feel free to offer your own take on this.
• It would be nice if most of the text could be fit to the poster.

```html
<!DOCTYPE html>
<html lang="en">
<head>
<meta charset="utf-8">
<title>VellumCheck – Professional Proofreading Services</title>
<link href="https://fonts.googleapis.com/css2?family=Montserrat:wght@400;500;600;700&family=Oswald:wght@400;500&display=swap" rel="stylesheet">
<style>
  :root{
    --teal:#2fae8f;
    --teal-light:#5cc7ad;
    --teal-dark:#23957a;
    --ink:#1f1a17;
    --panel:#1d1715;
    --paper:#ffffff;
    --backdrop:#eeeeec;
    --photo-a:#7a2a24;
    --photo-b:#2a1c1c;
    --photo-c:#c9a48e;
  }
  *{margin:0;padding:0;box-sizing:border-box}
  html,body{width:1200px;height:1000px;overflow:hidden;background:var(--backdrop)}
  body{font-family:"Montserrat",Arial,sans-serif;color:var(--ink)}
  .stage{position:relative;width:1200px;height:1000px}
  .flyer{
    position:absolute;left:270px;top:36px;width:547px;height:769px;
    transform:scale(1.2066);transform-origin:0 0;
    background:var(--paper);overflow:hidden;
    box-shadow:0 2px 10px rgba(0,0,0,.12);
  }
  .hero-photo{
    position:absolute;left:0;top:0;width:547px;height:325px;
    background:
      radial-gradient(ellipse at 40% 55%, var(--photo-c) 0%, rgba(201,164,142,0) 40%),
      radial-gradient(ellipse at 15% 30%, #b0302a 0%, rgba(176,48,42,0) 35%),
      linear-gradient(135deg, var(--photo-a) 0%, var(--photo-b) 70%);
  }
  .hero-shapes{position:absolute;left:0;top:0}
  .brand-badge{
    position:absolute;left:24px;top:45px;width:124px;height:124px;border-radius:50%;
    background:var(--teal);display:flex;align-items:center;justify-content:center;
  }
  .brand-badge span{color:#fff;font-size:17px;font-weight:500;letter-spacing:.2px}
  .headline{position:absolute;left:372px;top:112px;width:168px;color:#fff;font-family:"Oswald",Arial,sans-serif;}
  .headline h1{display:inline-block;font-size:29px;font-weight:400;line-height:36px;letter-spacing:0;
    border-bottom:2px solid #fff;padding-bottom:1px;white-space:nowrap}
  .headline h2{font-size:24px;font-weight:400;line-height:27px;margin-top:6px;letter-spacing:.3px}
  .intro-panel{
    position:absolute;left:0;top:325px;width:270px;height:180px;background:var(--panel);
    border-bottom-right-radius:14px;color:#fff;padding:12px 15px 0 23px;
    font-size:10.3px;line-height:15.5px;font-weight:500;
  }
  .intro-panel p{text-align:justify;margin-bottom:15px}
  .accent{color:var(--teal)}
  .price-guide{position:absolute;left:283px;top:337px;width:200px}
  .section-title{color:var(--teal);font-weight:700;font-size:14px;line-height:16px;letter-spacing:.2px}
  .checks{list-style:none}
  .price-guide .checks{margin-top:5px;font-size:8.7px;line-height:12.6px}
  .price-guide li{position:relative;padding-left:13px;margin-bottom:12px}
  .checks li svg{position:absolute;left:0;top:2px}
  .doc-types{position:absolute;left:23px;top:527px;width:240px}
  .doc-types .checks{margin-top:6px;font-size:9.3px;line-height:10.5px;font-weight:500}
  .doc-types li{position:relative;padding-left:13px;margin-bottom:8px}
  .testimonial{
    position:absolute;left:287px;top:593px;width:228px;height:78px;border-radius:12px;
    background:var(--teal);color:#fff;padding:9px 11px 0 10px;
  }
  .testimonial blockquote{font-size:7.9px;line-height:10.5px;text-align:justify}
  .testimonial cite{display:block;text-align:right;font-style:normal;font-size:5.6px;line-height:6.5px;margin-top:4px}
  .footer-backdrop{
    position:absolute;left:0;top:680px;width:547px;height:80px;
    background:linear-gradient(180deg, rgba(255,255,255,1) 0%, #f1eeec 60%, #f6e3e0 100%);
  }
  .contact{position:absolute;left:0;top:706px;width:547px;text-align:center}
  .contact .cta{font-size:12px;line-height:14px}
  .contact .cta strong{font-weight:700}
  .contact .details{font-size:17.5px;line-height:22px;font-weight:500;margin-top:3px;display:flex;justify-content:center;align-items:center;gap:8px}
  .footer-bar{position:absolute;left:0;bottom:0;width:547px;height:9px;background:var(--teal)}
</style>
</head>
<body>
<div class="stage">
  <div class="flyer">
    <div class="hero-photo" role="img" aria-label="Close-up photo of graduates in gowns holding rolled diplomas tied with red ribbon"></div>
    <svg class="hero-shapes" width="547" height="430" viewBox="0 0 547 430">
      <polygon points="355,0 547,0 547,60 400,45" fill="var(--teal-light)"/>
      <polygon points="277,177 400,45 547,60 547,422" fill="var(--teal)"/>
    </svg>

    <div class="brand-badge"><span>VellumCheck</span></div>

    <div class="headline">
      <h1>VELLUMCHECK</h1>
      <h2>PROFESSIONAL<br>PROOFREADING<br>SERVICES</h2>
    </div>

    <section class="intro-panel">
      <p>Help with English as a second language <span class="accent">(ESL - native English speaker with English Honours degree</span> will correct all English language errors, spelling and grammar mistakes.</p>
      <p>Includes referencing and editing for style, coherence and clarity</p>
      <p>Fast, negotiable time-frames.</p>
    </section>

    <section class="price-guide">
      <h3 class="section-title">PRICE GUIDE:</h3>
      <ul class="checks">
        <li><svg width="8" height="7" viewBox="0 0 8 7"><path d="M1 3.5l2 2L7 1" fill="none" stroke="var(--teal)" stroke-width="1.4"/></svg>Prices starting at <span class="accent">$20 per page.</span><br>Additional charges may apply for longer and/or more complex documents (e.g. documents requiring specialist help with English as a second language).</li>
        <li><svg width="8" height="7" viewBox="0 0 8 7"><path d="M1 3.5l2 2L7 1" fill="none" stroke="var(--teal)" stroke-width="1.4"/></svg>Discounts for not-for-profit organisations and students. <span class="accent">Special student discount rate: $25 per hour - roughly 1000 words (4 pages) of well-written text.</span></li>
        <li><svg width="8" height="7" viewBox="0 0 8 7"><path d="M1 3.5l2 2L7 1" fill="none" stroke="var(--teal)" stroke-width="1.4"/></svg>Package deals on documents <span class="accent">over 50,000 words.</span></li>
        <li><svg width="8" height="7" viewBox="0 0 8 7"><path d="M1 3.5l2 2L7 1" fill="none" stroke="var(--teal)" stroke-width="1.4"/></svg>Fast turnaround times (same day service can be provided by special arrangement).</li>
      </ul>
    </section>

    <section class="doc-types">
      <h3 class="section-title">TYPES OF PROOF-READ<br>DOCUMENTS:</h3>
      <ul class="checks">
        <li><svg width="9" height="8" viewBox="0 0 9 8"><path d="M1 4l2.3 2.3L8 1" fill="none" stroke="var(--teal)" stroke-width="1.6"/></svg>essays / assignments / theses / resumes</li>
        <li><svg width="9" height="8" viewBox="0 0 9 8"><path d="M1 4l2.3 2.3L8 1" fill="none" stroke="var(--teal)" stroke-width="1.6"/></svg>business correspondence / training manuals<br>/ newsletters</li>
        <li><svg width="9" height="8" viewBox="0 0 9 8"><path d="M1 4l2.3 2.3L8 1" fill="none" stroke="var(--teal)" stroke-width="1.6"/></svg>advertising copy / brochures / catalogues<br>/ media releases</li>
        <li><svg width="9" height="8" viewBox="0 0 9 8"><path d="M1 4l2.3 2.3L8 1" fill="none" stroke="var(--teal)" stroke-width="1.6"/></svg>websites / presentations / speeches</li>
        <li><svg width="9" height="8" viewBox="0 0 9 8"><path d="M1 4l2.3 2.3L8 1" fill="none" stroke="var(--teal)" stroke-width="1.6"/></svg>novels / short stories</li>
      </ul>
    </section>

    <aside class="testimonial">
      <blockquote>“Clara understood our requirements quickly and has been fantastic at delivering quality work, on time and within agreed budget. It's a pleasure to work with her.”</blockquote>
      <cite>Ruth Dalton<br>Operations Manager<br>northlineAU</cite>
    </aside>

    <div class="footer-backdrop" role="img" aria-label="Faded photo of a printed page with red proofreading marks"></div>
    <footer class="contact">
      <p class="cta">Contact Us For An <strong>Obligation-Free Quote:</strong></p>
      <p class="details">
        <svg width="13" height="13" viewBox="0 0 13 13"><circle cx="6.5" cy="6.5" r="5.6" fill="none" stroke="var(--teal)" stroke-width="1.2"/><path d="M4.3 3.6l1.1-.3.6 1.5-.7.6c.4.9 1 1.5 1.9 1.9l.6-.7 1.5.6-.3 1.1c-2.5.2-4.9-2.2-4.7-4.7z" fill="var(--teal)"/></svg>
        <span>0400 318 562</span><span>|</span><span>proofing@vellumcheck.com.au</span>
      </p>
    </footer>
    <div class="footer-bar"></div>
  </div>
</div>
</body>
</html>
```